exclusive Speakeasy Bar Web design in New Jersey USA

We are opening a speakeasy in New Jersey USA soon. we are looking for a web designer to do our web site including the coding. we a looking for a 4 to 5 page web design. the site will be mostly static. home page, contact page, menu page and a link to a 3rd party site (most likely Qelmo) for reservations. we are looking for this designer to do our menu deign as well. we are looking for a quick turnaround 7-10 days. i am attaching some pictures for the designers to see the concept design and the actual current pictures with our logo as well. professionally taken pictures will be provided later on. our photographer will be taking the pictures in the next week.

Industry/Entity Type

Restaurant, Bar, Speakeasy

Coding

Coded - Design and coding required

Number of Pages Required

4 page

Requirements
Must have
• home page, contact page, menu page and a link to qelmo.com for reservations
Nice to have
• some videos

```html
<!DOCTYPE html>
<html lang="en">
<head>
<meta charset="utf-8">
<title>219 Parlor — Speakeasy Bar in New Jersey</title>
<link rel="stylesheet" href="https://fonts.googleapis.com/css2?family=Abril+Fatface&family=Gentium+Book+Plus:ital,wght@0,400;0,700;1,400&family=Open+Sans:ital,wght@0,400;0,600;1,400&family=Poppins:wght@400;600&display=swap">
<style>
:root{
  --gold:#c9a15a;
  --gold-dark:#b58a43;
  --ink:#2a2a2a;
  --olive:#2f2a1a;
  --muted:#666;
  --cream:#faf5ee;
  --red:#f44d3a;
  --white:#fff;
}
*{margin:0;padding:0;box-sizing:border-box}
html,body{width:1200px;height:3049px;overflow:hidden}
body{position:relative;background:var(--white);font-family:"Open Sans",sans-serif;color:var(--ink)}
.abs{position:absolute}
a{color:inherit}
h1,h2,h3{font-weight:400}

/* header */
.brand{left:60px;top:10px;width:86px;height:110px;border:2px solid var(--gold);display:flex;align-items:center;justify-content:center;text-align:center;font-family:"Gentium Book Plus",serif;color:var(--olive);font-size:14px;line-height:1.2;letter-spacing:1px;background:var(--white);z-index:3}
.brand b{display:block;font-size:30px;font-weight:400;letter-spacing:0}
.nav{top:34px;left:661px;font-size:12.5px;text-transform:uppercase}
.nav a{text-decoration:none;position:absolute;white-space:nowrap}
.nav .active{color:var(--gold)}
.btn-outline{border:2px solid var(--gold);color:var(--gold);text-transform:uppercase;display:flex;align-items:center;justify-content:center;font-size:15px;letter-spacing:.5px;text-decoration:none}
.reserve-top{left:966px;top:20px;width:174px;height:45px}

/* hero */
.hero-photo{left:173px;top:86px;width:1027px;height:596px;background:
  radial-gradient(ellipse 80px 40px at 720px 180px,rgba(255,240,215,.85),transparent 70%),
  radial-gradient(ellipse 90px 30px at 80px 140px,rgba(240,230,215,.8),transparent 70%),
  radial-gradient(ellipse 220px 180px at 430px 250px,#6f9fb0 0%,#3c5e6c 55%,transparent 80%),
  radial-gradient(ellipse 260px 140px at 450px 440px,#3a2e3e,transparent 75%),
  radial-gradient(ellipse 200px 250px at 920px 330px,#8a6a48,transparent 75%),
  linear-gradient(180deg,#1c1f24 0%,#24313a 30%,#34424a 55%,#6a4a30 80%,#9a6a3a 100%)}
.hero-strip{left:0;top:86px;width:16px;height:596px;background:linear-gradient(#111,#444 45%,#ddd 60%,#666)}
.hero-card{left:16px;top:242px;width:491px;height:300px;background:var(--white)}
.hero-title{left:60px;top:296px;font-family:"Abril Fatface",serif;font-size:44px;line-height:49px;color:var(--olive);letter-spacing:1px}
.hero-sub{left:62px;top:407px;font-size:18px;color:#333}
.qelmo-btn{left:60px;top:448px;width:112px;height:49px;background:var(--red);color:var(--white);font-family:"Poppins",sans-serif;font-weight:600;font-size:24px;letter-spacing:5px;display:flex;align-items:center;justify-content:center;text-decoration:none}
.hero-arrows{left:186px;top:648px}

/* intro */
.intro-title{left:0;top:766px;width:1200px;text-align:center;font-family:"Gentium Book Plus",serif;font-size:34px;line-height:42px;color:var(--ink)}
.intro-title span{color:var(--gold)}
.vline{width:2px;background:var(--gold)}
.photo-bar{left:134px;top:966px;width:465px;height:265px;background:
  radial-gradient(ellipse 120px 50px at 110px 80px,rgba(220,150,80,.7),transparent 75%),
  radial-gradient(ellipse 120px 50px at 330px 85px,rgba(220,150,80,.7),transparent 75%),
  radial-gradient(ellipse 130px 50px at 110px 170px,rgba(190,110,60,.7),transparent 75%),
  radial-gradient(ellipse 130px 50px at 340px 170px,rgba(190,110,60,.7),transparent 75%),
  linear-gradient(180deg,#2a211a 0%,#4a3524 40%,#3a2a1e 75%,#1e1c1c 100%)}
.photo-lounge{left:558px;top:1030px;width:510px;height:337px;background:
  radial-gradient(ellipse 180px 70px at 230px 200px,#c88a3a,transparent 75%),
  radial-gradient(ellipse 120px 50px at 430px 150px,#b07a35,transparent 75%),
  radial-gradient(ellipse 100px 60px at 440px 270px,#55585c,transparent 75%),
  linear-gradient(180deg,#252525 0%,#3a3631 45%,#6a4a2c 70%,#5a4232 100%)}
.play{left:781px;top:1168px}
.intro-text{left:172px;top:1254px;width:340px;font-size:13px;line-height:22.5px;color:var(--muted)}
.about-link{left:172px;top:1337px;font-family:"Gentium Book Plus",serif;font-size:14px;color:var(--gold-dark)}

/* menu */
.section-title{left:0;width:1200px;text-align:center;font-family:"Gentium Book Plus",serif;color:var(--ink)}
.menu-sub{left:330px;top:1522px;width:540px;text-align:center;font-size:13.5px;line-height:23px;color:var(--gold)}
.tab{top:1594px;font-family:"Gentium Book Plus",serif;font-size:38px}
.tab-drink{left:478px;color:var(--gold)}
.tab-events{left:607px;color:transparent;-webkit-text-stroke:1px #e6dcc8}
.menu-img{width:187px;height:224px}
.img-champagne{background:radial-gradient(ellipse 22px 110px at 88px 120px,#1f3a24 0%,#2c4a2e 60%,transparent 100%),var(--cream)}
.img-vodka{background:radial-gradient(ellipse 28px 110px at 70px 120px,#c8c8c8 0%,#e2e2e2 60%,transparent 100%),radial-gradient(ellipse 32px 18px at 128px 128px,#7a3a1a,transparent 100%),var(--cream)}
.menu-heading{font-family:"Gentium Book Plus",serif;font-size:28px;letter-spacing:1px;text-transform:uppercase;color:var(--ink)}
.menu-list{list-style:none;font-size:14.5px;color:#333}
.menu-list li{position:absolute;left:0;white-space:nowrap;text-decoration:underline;text-underline-offset:3px}
.view-menu{left:509px;top:1987px;width:181px;height:45px}

/* banner */
.banner-photo{left:0;top:2114px;width:1125px;height:450px;background:
  radial-gradient(ellipse 260px 90px at 420px 360px,#c48634,transparent 75%),
  radial-gradient(ellipse 160px 70px at 180px 350px,#b67a30,transparent 75%),
  radial-gradient(ellipse 200px 120px at 900px 360px,#4a4d52,transparent 75%),
  radial-gradient(ellipse 260px 60px at 170px 300px,#1e1e1e,transparent 75%),
  linear-gradient(180deg,#2c2a27 0%,#3a3630 45%,#4a3a2a 75%,#2a2520 100%)}
.banner-title{left:742px;top:2262px;width:280px;text-align:center;font-family:"Gentium Book Plus",serif;font-size:38px;line-height:41px;color:var(--white);text-transform:uppercase}
.banner-btn{left:795px;top:2368px;width:173px;height:44px}

/* footer */
.footer-bg{left:0;top:2700px;width:1200px;height:349px;background:linear-gradient(180deg,#fff 0%,#f3f3f3 55%,#e8e8e8 100%)}
.info{width:300px;text-align:center}
.info h3{font-family:"Gentium Book Plus",serif;font-size:21px;margin-bottom:10px}
.info p{font-size:13.5px;line-height:21px;color:#444}
.footer-brand{left:558px;top:2738px;width:84px;height:110px}
.call{left:0;top:2870px;width:1200px;text-align:center;font-style:italic;font-size:17px;color:#333}
.social{top:2927px;width:36px;height:36px;border:1.5px solid var(--gold);display:flex;align-items:center;justify-content:center;font-size:9.5px;font-weight:600;color:var(--gold);text-decoration:none}
.copyright{left:0;top:2984px;width:1200px;text-align:center;font-family:"Poppins",sans-serif;font-size:12px;color:#555}
</style>
</head>
<body>

<header>
  <div class="abs brand"><span><b>219</b>PARLOR</span></div>
  <nav class="abs nav">
    <a class="active" style="left:0">Home</a>
    <a style="left:70px">Menu</a>
    <a style="left:134px">About</a>
    <a style="left:205px">Contact Us</a>
  </nav>
  <a class="abs btn-outline reserve-top">Reserve a Table</a>
</header>

<section class="hero">
  <div class="abs hero-strip" role="img" aria-label="Edge of the previous slide photo"></div>
  <div class="abs hero-photo" role="img" aria-label="Photo of the speakeasy lounge with velvet booths, globe lights and the backlit bar"></div>
  <div class="abs hero-card"></div>
  <h1 class="abs hero-title">QUALITY DRINK IN<br>NEW JERSEY</h1>
  <p class="abs hero-sub">Reserve your Table With</p>
  <a class="abs qelmo-btn">QELMO</a>
  <svg class="abs hero-arrows" width="70" height="20" viewBox="0 0 70 20" fill="none" stroke="#fff" stroke-width="1.5">
    <path d="M2 10H28M2 10l7-6M2 10l7 6" opacity=".7"/>
    <path d="M40 10H66M66 10l-7-6M66 10l-7 6"/>
  </svg>
</section>

<section class="intro">
  <h2 class="abs intro-title">The most satisfying Speakeasy Bar experience<br><span>anyone can have in 219 Parlor</span></h2>
  <div class="abs vline" style="left:599px;top:872px;height:44px"></div>
  <div class="abs photo-bar" role="img" aria-label="Photo of the back bar shelves stocked with bottles"></div>
  <div class="abs photo-lounge" role="img" aria-label="Video still of the mural room with tufted amber chairs"></div>
  <svg class="abs play" width="64" height="64" viewBox="0 0 64 64">
    <circle cx="32" cy="32" r="30" fill="#fff" opacity=".95"/>
    <circle cx="32" cy="32" r="26" fill="none" stroke="#c9a15a" stroke-width="2"/>
    <path d="M25 19L46 32L25 45Z" fill="#c9a15a"/>
  </svg>
  <p class="abs intro-text">Whether it is for a few low-key drinks with friends or a romantic rendezvous, Speakeasy provides the perfect backdrop with its dark art-work walls...</p>
  <a class="abs about-link">About Us</a>
</section>

<section class="menu">
  <div class="abs vline" style="left:598px;top:1420px;height:45px"></div>
  <h2 class="abs section-title" style="top:1472px;font-size:30px">Menu</h2>
  <p class="abs menu-sub">We also create “Whatever You say” which is a bespoke cocktail experience made for you, as per your choice of the base as well as flavour.</p>
  <span class="abs tab tab-drink">Drink</span>
  <span class="abs tab tab-events">Events</span>

  <div class="abs menu-img img-champagne" style="left:60px;top:1700px" role="img" aria-label="Photo of a champagne bottle"></div>
  <h3 class="abs menu-heading" style="left:273px;top:1694px">Cocktails</h3>
  <ul class="abs menu-list" style="left:276px;top:1750px">
    <li style="top:0">French Spritz</li>
    <li style="top:40px">Salted Caramel Espresso Martini</li>
    <li style="top:85px">Flat White Martini</li>
    <li style="top:127px">Coconut Martini</li>
    <li style="top:172px">Dark &amp; Stormy</li>
  </ul>

  <div class="abs menu-img img-vodka" style="left:560px;top:1700px" role="img" aria-label="Photo of a vodka bottle beside a martini glass"></div>
  <h3 class="abs menu-heading" style="left:774px;top:1694px">Mocktails</h3>
  <ul class="abs menu-list" style="left:776px;top:1750px">
    <li style="top:0">Canela</li>
    <li style="top:40px">Orgeat Lemonade</li>
    <li style="top:85px">Beautiful Kathmandu</li>
    <li style="top:127px">Paloma Inferno</li>
    <li style="top:172px">Sultry Stare</li>
  </ul>

  <a class="abs btn-outline view-menu">View Full Menu</a>
</section>

<section class="banner">
  <div class="abs banner-photo" role="img" aria-label="Photo of the mural lounge with a leather sofa and amber armchairs"></div>
  <h2 class="abs banner-title">Our Pictures Speak For Us</h2>
  <a class="abs btn-outline banner-btn">Reserve a Table</a>
</section>

<footer>
  <div class="abs footer-bg"></div>
  <div class="abs vline" style="left:599px;top:2605px;height:45px"></div>
  <h2 class="abs section-title" style="top:2660px;font-size:34px">Say Hello To Us</h2>
  <div class="abs info" style="left:124px;top:2756px"><h3>Address</h3><p>219 Parlor<br>speakeasy in New Jersey USA</p></div>
  <div class="abs brand footer-brand"><span><b>219</b>PARLOR</span></div>
  <div class="abs info" style="left:775px;top:2756px"><h3>Opening Hours</h3><p>Every Day<br>5:00 PM - 12:00 AM</p></div>
  <p class="abs call">Call Us 123 456 7890</p>
  <a class="abs social" style="left:538px">Lumo</a>
  <a class="abs social" style="left:582px">Pixo</a>
  <a class="abs social" style="left:625px">Trill</a>
  <p class="abs copyright">©219 Parlor - 2023 All rights reserved.</p>
</footer>

</body>
</html>
```